Corvantel, LLC Website

Creating website for medical billing company.

Target Market(s)

Medical providers

Industry/Entity Type

Medical billing

Coding

Coded - Design and coding required

Number of Pages Required

3 page

Font styles to use
Other font styles liked:
• Fonts that match our logo.

Requirements
Must have
• First page (greeting and explanation of who we are). Second page something about me and company (I'll supply some content, make generic for now). And page three, information that people can give for us to contact them.
Nice to have
• A little animation. But not over-the-top. Colors that match our logo.
Should not have
• Over-the-top animation.

```html
<!DOCTYPE html>
<html lang="en">
<head>
<meta charset="utf-8">
<title>Corvantel, LLC – Medical Billing</title>
<link href="https://fonts.googleapis.com/css2?family=Open+Sans:wght@400;600;700;800&display=swap" rel="stylesheet">
<style>
:root{
  --navy:#0d1b3e;
  --navy-deep:#08122b;
  --teal:#14a6c9;
  --teal-dark:#0b86a8;
  --ink:#1a1f36;
  --muted:#6b7280;
  --light:#f3f4f6;
  --white:#ffffff;
  --line:#d9dde5;
}
*{box-sizing:border-box;margin:0;padding:0}
html,body{width:1200px;height:4692px;overflow:hidden}
body{font-family:"Open Sans",Arial,sans-serif;color:var(--ink);background:var(--white);position:relative}
.abs{position:absolute}
.eyebrow{font-size:13px;font-weight:700;letter-spacing:1.5px;text-transform:uppercase;color:var(--teal)}
.btn{display:inline-flex;align-items:center;gap:10px;background:var(--teal);color:var(--white);font-weight:700;font-size:15px;padding:12px 26px;border-radius:4px}
.center{left:0;width:1200px;text-align:center}

/* hero */
.hero{top:0;left:0;width:1200px;height:940px;background:linear-gradient(160deg,#3a4150 0%,#232a38 45%,#161c28 100%)}
.topbar{top:8px;left:120px;width:960px;display:flex;justify-content:space-between;font-size:13px;color:#d6dbe4}
.topbar .contacts{display:flex;gap:26px;align-items:center}
.topbar .social{display:flex;gap:10px}
.topbar .social span{width:12px;height:12px;background:#cfd6e0;border-radius:2px}
.brand{display:flex;align-items:center;gap:10px;font-weight:700;color:var(--white);font-size:22px}
.brand .mark{width:34px;height:34px;border-radius:50%;background:var(--teal)}
.badges{top:56px;left:780px;display:flex;gap:36px;color:var(--white);font-size:14px;font-weight:700;line-height:1.25}
.badges .b{display:flex;gap:10px;align-items:center}
.badges .ic{width:34px;height:34px;border-radius:50%;border:2px solid var(--teal)}
.nav{top:136px;left:120px;width:960px;height:54px;background:var(--white);display:flex;align-items:center;padding:0 20px;box-shadow:0 4px 18px rgba(0,0,0,.25)}
.nav a{font-size:15px;font-weight:600;color:var(--ink);text-decoration:none;width:150px;text-align:center;padding:8px 0}
.nav a.active{background:var(--white);box-shadow:0 0 0 1px var(--line);border-radius:3px}
.nav .btn{margin-left:auto;font-size:13px;padding:9px 18px;border-radius:20px}
.hero h1{top:528px;font-size:64px;line-height:1.15;font-weight:700;color:var(--white)}
.hero .eyebrow{top:486px;color:#cfe9f2}

/* about */
.photo{background:linear-gradient(135deg,#7b8794,#3e4a5c);}
.about-photo{top:988px;left:92px;width:360px;height:360px;border-radius:50%;border:8px solid var(--navy)}
.about-badge{top:1284px;left:400px;width:84px;height:84px;border-radius:50%;background:var(--white);border:4px solid var(--teal);display:flex;align-items:center;justify-content:center}
.about-badge span{width:34px;height:34px;border-radius:50%;background:var(--navy)}
.about-text{top:960px;left:612px;width:480px}
.about-text h2{font-size:38px;line-height:1.25;color:var(--navy);font-weight:800;margin:14px 0 18px}
.about-text h3{font-size:19px;color:var(--teal-dark);font-weight:700;margin-bottom:16px}
.about-text p{font-size:14px;line-height:1.6;color:var(--muted);margin-bottom:18px}

/* services */
.services{top:1440px;left:0;width:1200px;height:560px;background:var(--light)}
.sec-title{font-size:40px;font-weight:700;color:var(--navy)}
.card{top:188px;width:316px;height:312px;background:var(--white);text-align:center;padding:44px 30px 0;border-bottom:4px solid transparent}
.card h4{font-size:19px;font-weight:600;color:var(--navy);margin:18px 0 22px}
.card p{font-size:14px;line-height:1.6;color:var(--ink)}
.card.feature{background:linear-gradient(160deg,#5b6472,#1f2634);border-bottom-color:var(--teal);color:var(--white);padding-top:120px}
.card.feature h4,.card.feature p{color:var(--white)}

/* call band */
.callband{top:2000px;left:0;width:1200px;height:364px;background:linear-gradient(180deg,#2c313c,#1a1f29)}
.callband h2{top:118px;font-size:34px;font-weight:600;color:var(--white);line-height:1.35}
.callband h2 em{font-style:normal;color:var(--teal)}
.callstrip{top:276px;left:352px;width:600px;height:44px;background:var(--white);border-radius:4px;display:flex;align-items:center;justify-content:space-around;font-size:15px;font-weight:600;color:var(--ink)}

/* why */
.why{top:2364px;left:0;width:1200px;height:604px;background:var(--light)}
.why-item{width:240px;font-size:14px;line-height:1.5;color:var(--muted)}
.why-item h5{font-size:18px;font-weight:700;color:var(--navy);margin-bottom:4px}
.why-item.right{text-align:left}
.why-item.left{text-align:left}
.why-ic{width:48px;height:48px;border-radius:50%;background:var(--white);border:1px solid var(--line);display:flex;align-items:center;justify-content:center}

/* testimonials */
.testi{top:2968px;left:0;width:1200px;height:612px;background:linear-gradient(180deg,#262b36,#151a24)}
.tcard{top:152px;width:328px;height:320px;text-align:center;padding-top:80px}
.tcard.white{background:var(--white);border-bottom:5px solid var(--teal)}
.tcard.dark{background:var(--navy);border-bottom:5px solid var(--teal)}
.tcard h6{font-size:17px;font-weight:700}
.tcard .stars{color:#e53935;font-size:16px;letter-spacing:3px;margin:4px 0 16px}
.tcard p{font-size:14px;line-height:1.6;padding:0 30px}
.tcard .q{font-size:56px;font-weight:800;color:var(--teal);line-height:1;margin-top:18px}
.tcard.dark h6,.tcard.dark p{color:var(--white)}
.avatar{position:absolute;top:-28px;left:50%;margin-left:-40px;width:80px;height:80px;border-radius:50%;border:4px solid var(--white);background:linear-gradient(135deg,#8a94a3,#4a5568)}

/* contact */
.contact h2{top:3648px;left:108px;font-size:44px;font-weight:600;color:var(--navy)}
.contact h2 span{font-weight:400}
.cinfo{left:124px;display:flex;gap:20px;align-items:center}
.cinfo .ic{width:40px;height:40px;display:flex;align-items:center;justify-content:center}
.cinfo b{display:block;font-size:13px;color:var(--navy);font-weight:700}
.cinfo span{font-size:13px;color:var(--muted)}
.form{top:3660px;left:600px;width:500px;height:532px;background:var(--white);border-top:6px solid var(--teal);box-shadow:0 6px 24px rgba(0,0,0,.12);padding:30px 40px}
.form h3{font-size:26px;font-weight:600;color:var(--navy);margin-bottom:28px}
.form label{display:block;font-size:13px;font-weight:600;color:var(--ink);margin-bottom:6px}
.field{height:36px;border:1px solid var(--line);border-radius:20px;font-size:12px;color:#9aa1ad;padding:9px 16px;margin-bottom:18px}
.form .row{display:flex;gap:20px}.form .row>div{flex:1}
.field.area{height:124px;border-radius:6px}

/* footer */
.footer{top:4250px;left:0;width:1200px;height:442px;background:var(--navy-deep);color:#c5ccd8}
.fcol h4{font-size:16px;font-weight:700;color:var(--white);margin-bottom:16px}
.fcol li{list-style:none;font-size:13px;line-height:1.85}
.fsocial{display:flex;gap:10px;margin-top:18px}
.fsocial span{width:28px;height:28px;background:var(--teal);border-radius:3px}
.newsletter{display:flex;margin-top:16px}
.newsletter .in{width:200px;height:40px;background:var(--white);font-size:12px;color:#9aa1ad;padding:12px 14px}
.newsletter .go{width:44px;height:40px;background:var(--teal);display:flex;align-items:center;justify-content:center}
.finfo{top:316px;left:0;width:1200px;display:flex;justify-content:center;gap:60px;padding-top:26px;border-top:1px solid #22305a}
.finfo .it{display:flex;gap:12px;align-items:center;width:200px}
.finfo .ic{width:44px;height:44px;border-radius:50%;background:#1d2a52;display:flex;align-items:center;justify-content:center}
.finfo b{display:block;font-size:14px;color:var(--white)}
.finfo span{font-size:12px}
.copyright{top:410px;left:0;width:1200px;height:32px;background:#050b1c;text-align:center;font-size:12px;font-weight:700;letter-spacing:1px;color:var(--white);line-height:32px}
</style>
</head>
<body>

<!-- HERO -->
<section class="abs hero" role="img" aria-label="Photo of a medical billing office team at work, darkened">
</section>
<div class="abs topbar">
  <div class="contacts">
    <span>☏ +(001) 555-0142</span><span>✉ hello@corvantel-mail.com</span><span>☏ 555-0148</span>
  </div>
  <div class="social"><span></span><span></span><span></span><span></span></div>
</div>
<div class="abs brand" style="top:58px;left:120px"><span class="mark"></span>Corvantel, LLC</div>
<div class="abs badges">
  <div class="b"><span class="ic"></span>24/7<br>Service</div>
  <div class="b"><span class="ic"></span>Qualified<br>Professionals</div>
</div>
<nav class="abs nav">
  <a class="active">Home</a><a>About Us</a><a>Services</a><a>Blog</a><a>Contact</a>
  <span class="btn">Get A Quote</span>
</nav>
<div class="abs center eyebrow hero-eyebrow" style="top:486px;color:#d3ecf5">Medical Billing Services</div>
<h1 class="abs center" style="top:528px;font-size:64px;line-height:1.15;font-weight:700;color:#fff">Where Efficiency<br>Meets Profitability.</h1>
<div class="abs" style="top:736px;left:544px"><span class="btn" style="padding:10px 24px;font-size:14px">About Us</span></div>
<svg class="abs" style="top:760px;left:0" width="1200" height="190" viewBox="0 0 1200 190">
  <path d="M0 80 C300 200 800 150 1200 20 L1200 190 L0 190 Z" fill="#fff"/>
  <path d="M0 80 C300 200 800 150 1200 20" fill="none" stroke="#14a6c9" stroke-width="14"/>
  <path d="M0 104 C320 210 820 160 1200 44" fill="none" stroke="#0b86a8" stroke-width="4" opacity=".6"/>
</svg>

<!-- ABOUT -->
<div class="abs photo about-photo" role="img" aria-label="Photo of two colleagues reviewing documents on a tablet"></div>
<div class="abs about-badge"><span></span></div>
<div class="abs about-text">
  <div class="eyebrow">Who We Are</div>
  <h2>The team you can trust<br>to get the job done</h2>
  <h3>Billing Solutions for Medical Success.</h3>
  <p>Lorem ipsum dolor sit amet, consectetur adipiscing elit, sed do eiusmod tempor incididunt ut labore et dolore magna aliqua. Ut enim ad minim veniam, quis nostrud exercitation ullamco laboris nisi ut aliquip ex commodo consequat.</p>
  <p>Lorem ipsum dolor sit amet, consectetur adipiscing elit, sed do eiusmod tempor incididunt ut labore et dolore magna aliqua.</p>
  <span class="btn" style="margin-top:10px">Contact us <span>→</span></span>
</div>

<!-- SERVICES -->
<section class="abs services">
  <div class="abs center eyebrow" style="top:56px">Our Services</div>
  <h2 class="abs center sec-title" style="top:82px">Services We Offer</h2>
  <div class="abs card feature" style="left:92px" role="img" aria-label="Photo of a smiling audit support specialist">
    <h4>Audit Support</h4>
    <p>Lorem ipsum dolor sit amet, consectetur adipiscing elit, sed do eiusmod</p>
  </div>
  <div class="abs card" style="left:440px">
    <svg width="52" height="52" viewBox="0 0 52 52"><circle cx="26" cy="26" r="22" fill="none" stroke="#14a6c9" stroke-width="2.5"/><path d="M16 34 L24 24 L30 30 L38 18" fill="none" stroke="#14a6c9" stroke-width="2.5"/></svg>
    <h4>Reporting and Analytics</h4>
    <p>Lorem ipsum dolor sit amet, consectetur adipiscing elit, sed do eiusmod tempor</p>
  </div>
  <div class="abs card" style="left:784px">
    <svg width="52" height="52" viewBox="0 0 52 52"><path d="M26 4 L32 19 L48 20 L36 31 L40 47 L26 38 L12 47 L16 31 L4 20 L20 19 Z" fill="none" stroke="#14a6c9" stroke-width="2.5"/></svg>
    <h4>Patient Billing and Invoicing</h4>
    <p>Lorem ipsum dolor sit amet, consectetur adipiscing elit, sed do eiusmod tempor</p>
  </div>
</section>

<!-- CALL BAND -->
<section class="abs callband" role="img" aria-label="Dimmed photo of a busy medical office">
  <h2 class="abs center">We're On <em>Call 24/7</em> to React Promptly to Your<br>Medical Billing Needs</h2>
  <div class="abs callstrip"><span>☏ +(001) 555-0142</span><span>|</span><span>✉ info@corvantel-mail.com</span></div>
</section>

<!-- WHY CHOOSE US -->
<section class="abs why">
  <div class="abs center eyebrow" style="top:36px">Why Choose Us</div>
  <h2 class="abs center sec-title" style="top:62px">Why Choose Us</h2>
  <svg class="abs" style="top:170px;left:380px" width="440" height="440" viewBox="0 0 440 440">
    <circle cx="220" cy="220" r="168" fill="none" stroke="#0d1b3e" stroke-width="2"/>
    <circle cx="220" cy="220" r="132" fill="#fff" stroke="#0d1b3e" stroke-width="6"/>
  </svg>
  <div class="abs brand" style="top:352px;left:520px;color:#0d1b3e;font-size:24px;flex-direction:column;gap:8px"><span class="mark" style="width:44px;height:44px;background:#0d1b3e"></span>Corvantel</div>
  <div class="abs why-ic" style="top:192px;left:436px">✚</div>
  <div class="abs why-ic" style="top:192px;left:716px">✓</div>
  <div class="abs why-ic" style="top:336px;left:362px">✓</div>
  <div class="abs why-ic" style="top:336px;left:790px">✚</div>
  <div class="abs why-ic" style="top:474px;left:436px">★</div>
  <div class="abs why-ic" style="top:474px;left:716px">☏</div>
  <div class="abs why-item left" style="top:176px;left:148px"><h5>Expertise &amp; Experience</h5>Lorem ipsum dolor sit amet,<br>consectetur adipiscing elit</div>
  <div class="abs why-item left" style="top:296px;left:132px"><h5>Research Capabilities</h5>Lorem ipsum dolor sit amet,<br>consectetur adipiscing elit</div>
  <div class="abs why-item left" style="top:412px;left:148px"><h5>Quality Assurance</h5>Lorem ipsum dolor sit amet,<br>consectetur adipiscing elit</div>
  <div class="abs why-item right" style="top:176px;left:832px"><h5>Customization</h5>Lorem ipsum dolor sit amet,<br>consectetur adipiscing elit</div>
  <div class="abs why-item right" style="top:296px;left:872px"><h5>Cost-Effective</h5>Lorem ipsum dolor sit amet,<br>consectetur adipiscing elit</div>
  <div class="abs why-item right" style="top:412px;left:832px"><h5>Client-Centric</h5>Lorem ipsum dolor sit amet,<br>consectetur adipiscing elit</div>
</section>

<!-- TESTIMONIALS -->
<section class="abs testi" role="img" aria-label="Dimmed photo of healthcare staff in a hallway">
  <div class="abs center eyebrow" style="top:56px;color:#fff">Testimonials</div>
  <h2 class="abs center sec-title" style="top:84px;color:#fff">What Clients are saying</h2>
  <div class="abs tcard white" style="left:96px"><div class="avatar" role="img" aria-label="Client portrait"></div><h6>Harlan Brooke</h6><div class="stars">★★★★★</div><p>Lorem ipsum dolor sit amet consectetur adip elit, sed do eiusmod tempor incididunt ut labore et dolore magna aliqua.</p><div class="q">“</div></div>
  <div class="abs tcard dark" style="left:436px"><div class="avatar" role="img" aria-label="Client portrait"></div><h6>Mira Castell</h6><div class="stars">★★★★★</div><p>Lorem ipsum dolor sit amet consectetur adip elit, sed do eiusmod tempor incididunt ut labore et dolore magna aliqua.</p><div class="q">“</div></div>
  <div class="abs tcard dark" style="left:776px"><div class="avatar" role="img" aria-label="Client portrait"></div><h6>Devon Ashby</h6><div class="stars">★★★★★</div><p>Lorem ipsum dolor sit amet consectetur adip elit, sed do eiusmod tempor incididunt ut labore et dolore magna aliqua.</p><div class="q">“</div></div>
  <svg class="abs" style="top:516px;left:576px" width="48" height="10"><circle cx="8" cy="5" r="4" fill="#fff"/><circle cx="24" cy="5" r="4" fill="#777"/><circle cx="40" cy="5" r="4" fill="#777"/></svg>
</section>

<!-- CONTACT -->
<section class="contact">
  <h2 class="abs">Contact Us <span>Today</span></h2>
  <div class="abs cinfo" style="top:3730px"><div class="ic"><svg width="30" height="30" viewBox="0 0 30 30"><path d="M15 3a9 9 0 0 0-9 9c0 7 9 15 9 15s9-8 9-15a9 9 0 0 0-9-9z" fill="none" stroke="#14a6c9" stroke-width="2"/><circle cx="15" cy="12" r="3" fill="#14a6c9"/></svg></div><div><b>HEAD OFFICE</b><span>21 Lorem Ipsum ABC 123</span></div></div>
  <div class="abs cinfo" style="top:3802px"><div class="ic"><svg width="30" height="30" viewBox="0 0 30 30"><rect x="3" y="7" width="24" height="16" fill="none" stroke="#14a6c9" stroke-width="2"/><path d="M3 7 L15 17 L27 7" fill="none" stroke="#14a6c9" stroke-width="2"/></svg></div><div><b>EMAIL ADDRESS</b><span>hello@corvantel-mail.com</span></div></div>
  <div class="abs cinfo" style="top:3874px"><div class="ic"><svg width="30" height="30" viewBox="0 0 30 30"><path d="M8 4 L12 4 L14 10 L11 12 C12 16 14 18 18 19 L20 16 L26 18 L26 22 C26 24 24 26 22 26 C13 25 5 17 4 8 C4 6 6 4 8 4 Z" fill="none" stroke="#14a6c9" stroke-width="2"/></svg></div><div><b>CALL US NOW</b><span>Call Now: 555-0148</span></div></div>
  <div class="abs form">
    <h3>Send Us A Message</h3>
    <div class="row"><div><label>First Name</label><div class="field">John</div></div><div><label>Last Name</label><div class="field">Doe</div></div></div>
    <label>Email</label><div class="field">info@corvantel-mail.com</div>
    <label>Message</label><div class="field area">Type Your Message</div>
    <span class="btn" style="padding:10px 22px;font-size:14px">Contact us <span>→</span></span>
  </div>
</section>

<!-- FOOTER -->
<svg class="abs" style="top:4150px;left:0" width="1200" height="110" viewBox="0 0 1200 110">
  <path d="M0 20 C260 130 700 110 1200 40 L1200 110 L0 110 Z" fill="#08122b"/>
  <path d="M0 10 C260 120 700 100 1200 30" fill="none" stroke="#14a6c9" stroke-width="12"/>
</svg>
<footer class="abs footer">
  <div class="abs fcol" style="top:20px;left:120px;width:300px">
    <div class="brand" style="font-size:22px;margin-bottom:16px"><span class="mark"></span>Corvantel, LLC</div>
    <li>Lorem ipsum dolor sit amet, consectetur adipiscing elit, sed do eiusmod tempor incididunt ut labore.</li>
    <div class="fsocial"><span></span><span></span><span></span><span></span></div>
  </div>
  <div class="abs fcol" style="top:36px;left:488px"><h4>Quick Links</h4><li>Home</li><li>Services</li><li>About Us</li><li>Contact</li><li>Blog</li><li>Testimonials</li></div>
  <div class="abs fcol" style="top:76px;left:640px"><li>Cookies Policy</li><li>Terms of Use</li><li>Careers</li><li>Our Team</li><li>News</li></div>
  <div class="abs fcol" style="top:36px;left:824px;width:260px"><h4>Newsletters</h4><li style="line-height:1.6">Lorem ipsum dolor sit amet, consectetur adipiscing elit sed do.</li>
    <div class="newsletter"><div class="in">Enter Email Address</div><div class="go"><svg width="14" height="14" viewBox="0 0 14 14"><path d="M3 1 L11 7 L3 13 Z" fill="#fff"/></svg></div></div></div>
  <div class="abs finfo">
    <div class="it"><div class="ic"><svg width="20" height="20" viewBox="0 0 30 30"><path d="M15 3a9 9 0 0 0-9 9c0 7 9 15 9 15s9-8 9-15a9 9 0 0 0-9-9z" fill="none" stroke="#14a6c9" stroke-width="2.5"/></svg></div><div><b>Address</b><span>101 Maple Road</span></div></div>
    <div class="it"><div class="ic"><svg width="20" height="20" viewBox="0 0 30 30"><rect x="3" y="7" width="24" height="16" fill="none" stroke="#14a6c9" stroke-width="2.5"/><path d="M3 7 L15 17 L27 7" fill="none" stroke="#14a6c9" stroke-width="2.5"/></svg></div><div><b>Email Us</b><span>support@corvantel-mail.com</span></div></div>
    <div class="it"><div class="ic"><svg width="20" height="20" viewBox="0 0 30 30"><path d="M8 4 L12 4 L14 10 L11 12 C12 16 14 18 18 19 L20 16 L26 18 L26 22 C26 24 24 26 22 26 C13 25 5 17 4 8 C4 6 6 4 8 4 Z" fill="none" stroke="#14a6c9" stroke-width="2.5"/></svg></div><div><b>Contact Us</b><span>+(001) 555-0142</span></div></div>
    <div class="it"><div class="ic"><svg width="20" height="20" viewBox="0 0 30 30"><circle cx="15" cy="15" r="11" fill="none" stroke="#14a6c9" stroke-width="2.5"/><path d="M15 8 V15 L20 18" fill="none" stroke="#14a6c9" stroke-width="2.5"/></svg></div><div><b>Opening Hour</b><span>Mon – Friday 10 am – 6 pm</span></div></div>
  </div>
  <div class="abs copyright">CORVANTEL MEDICAL BILLING</div>
</footer>

</body>
</html>
```